Vantor - Adventurous, Fun, Exciting, Social Fitness Club needs a Webpage with attitude!

Vantor... we're a fun, social, outdoor fitness club that needs not just a homepage designed for our website, but in the process a "personality" for our unique, innovative and cheeky brand.
We pride ourselves on getting our members outdoors trying new, exciting physical activities in an effort to find joy in an active lifestyle, and sharing that experience with other like minded people. We offer:
- Personal Training (1-on-1 Fitness Training)
- Group Fitness Classes (Boxing, Pilates, etc)
- Boot Camps (Military Style - Sandbags, Ropes, Tyres, etc)
- Events (Fun Runs, Triathlons, Ocean Swims, Treks, etc)
- Adventures(Machu Picchu Trek, Rock Climbing, Kayaking, etc)
Our tag line is 'No Judgements. No Limits!' The homepage should be exciting, adventurous and innovative, illustrating the values of our brand: possibility, thirst for life, personal accomplishment & freedom. It should be fun, friendly & inviting.
A few of our key benefits to members are:
- No Boring Workouts
- No Joining Fees or Long Term Contracts
- Results Guaranteed
The links below should give you a rough idea of the sort of "feel" we're after (vibrant, active, adventurous ).
http://www.pupiljourneys.com.au/
http://www.layoutgoblin.com/website-templates/31924.html
http://www.layoutgoblin.com/website-templates/32751.html
http://www.pivel.com/
Target Market(s)
Real, Everyday People - Men & Women (30:70) aged mainly between 21-40, who want a more exciting and enjoyable fitness experience than your typical gym offers.
Industry/Entity Type
Fitness
Requirements
Must have
- Strong, uplifting and motivating images of people enjoying fitness/physical activities outdoors

```html
<!DOCTYPE html>
<html lang="en">
<head>
<meta charset="utf-8">
<title>Vantor – No Judgements. No Limits!</title>
<link href="https://fonts.googleapis.com/css2?family=Ubuntu:wght@400;500;700&family=Arimo:wght@400;700&display=swap" rel="stylesheet">
<style>
:root{
  --orange:#f7941d;
  --orange-deep:#e8650c;
  --yellow:#ffd400;
  --black:#111;
  --panel:#1d1d1d;
  --white:#fff;
  --paper:#f2f1ee;
  --text:#222;
  --link:#f47a00;
  --jungle-dark:#1f3a14;
  --jungle-light:#9fb58a;
}
*{box-sizing:border-box;margin:0;padding:0}
html,body{width:1037px;height:1200px;overflow:hidden}
body{position:relative;font-family:"Arimo",sans-serif;color:var(--text)}
.backdrop{position:absolute;inset:0;background:linear-gradient(180deg,var(--jungle-light) 0%,#5f7d46 30%,var(--jungle-dark) 75%,#12250b 100%)}
.abs{position:absolute}
.brand{left:124px;top:30px;display:flex;align-items:center;gap:8px;width:196px;white-space:nowrap}
.brand-dot{width:22px;height:22px;border-radius:50%;background:var(--orange);flex:none}
.brand-name{font-family:"Ubuntu",sans-serif;font-weight:700;font-size:40px;color:var(--orange);line-height:1}
.tagline{left:330px;top:45px;font-family:"Ubuntu",sans-serif;font-weight:700;font-size:21px;color:var(--orange-deep);white-space:nowrap}
.account{left:828px;top:9px;font-size:10.5px;font-family:"Ubuntu",sans-serif;color:var(--black)}
.account span{margin:0 7px}
.phone{left:722px;top:28px;width:201px;height:21px;background:var(--black);border-radius:3px;display:flex;align-items:center;padding-left:8px;gap:10px}
.phone-icon{width:26px;height:26px;margin-top:-4px;background:var(--orange);border-radius:4px;display:flex;align-items:center;justify-content:center}
.phone-num{font-family:"Ubuntu",sans-serif;font-weight:700;font-size:20px;color:var(--orange)}
.page{left:114px;top:65px;width:809px;height:1110px;background:var(--white);border-radius:6px}
.header-band{left:118px;top:69px;width:801px;height:54px;background:var(--paper)}
.tools{left:618px;top:83px;display:flex;align-items:center;gap:8px;font-family:"Ubuntu",sans-serif;font-size:10.5px;color:var(--black)}
.clock{width:20px;height:20px;border:2px solid var(--black);border-radius:50%;position:relative}
.clock:after{content:"";position:absolute;left:7px;top:3px;width:4px;height:6px;border-left:2px solid var(--black);border-bottom:2px solid var(--black)}
.select{width:106px;height:18px;background:var(--black);color:var(--white);font-size:10px;padding:2px 7px;border-radius:2px;display:flex;justify-content:space-between}
.nav{left:114px;top:125px;width:809px;height:33px;background:var(--black);display:flex;align-items:center}
.nav a{font-family:"Ubuntu",sans-serif;font-size:10.5px;color:var(--orange);text-decoration:none;padding:0 27px;height:33px;line-height:33px;border-right:1px solid #333}
.nav a.active{background:var(--orange);color:var(--black);margin:0 8px 0 9px;height:22px;line-height:22px;padding:0 21px;border:none}
.social{left:828px;top:133px;display:flex;gap:5px}
.social span{width:18px;height:18px;border-radius:3px;background:#3a7bd5}
.social span:last-child{background:var(--orange)}
.hero{left:120px;top:164px;width:798px;height:280px;background:var(--black)}
.hero-photo{left:127px;top:171px;width:509px;height:265px;background:linear-gradient(135deg,#2e6fc4 0%,#4fa3e0 45%,#8a9a3c 75%,#2a4d8c 100%)}
.hero-caption{left:127px;top:371px;width:509px;height:65px;background:rgba(0,0,0,.72);padding:6px 12px}
.hero-caption h2{font-family:"Ubuntu",sans-serif;font-weight:700;font-size:20px;color:var(--orange)}
.hero-caption p{font-size:10px;color:var(--white);line-height:12px;margin-top:3px}
.offer{left:636px;top:171px;width:282px;height:265px;background:linear-gradient(180deg,#2a1d08 0%,#111 45%)}
.offer h3{position:absolute;left:18px;top:12px;font-family:"Ubuntu",sans-serif;font-weight:700;line-height:1}
.offer .g{font-size:19px;color:var(--orange)}
.offer .f{font-size:27px;color:var(--white);display:block}
.offer .t{font-size:19px;color:var(--orange)}
.snaps{position:absolute;left:14px;top:84px;display:flex;gap:12px}
.snaps div{width:53px;height:50px;border:4px solid var(--white);background:linear-gradient(135deg,#6c8fb0,#b6763f)}
.snaps div:nth-child(1){transform:rotate(-5deg)}.snaps div:nth-child(3){background:#e8a422;transform:rotate(3deg)}.snaps div:nth-child(4){transform:rotate(-8deg);background:linear-gradient(135deg,#999,#c33)}
.perks{position:absolute;left:0;right:0;top:155px;text-align:center;font-size:8.5px;font-weight:700;color:var(--white);line-height:10.6px}
.perks b{color:var(--orange)}
.field{position:absolute;height:21px;background:var(--white);border-radius:3px;font-size:9.5px;color:#444;padding:4px 13px}
.join{position:absolute;left:174px;top:235px;width:96px;height:22px;background:linear-gradient(var(--yellow),var(--orange));border-radius:4px;font-family:"Ubuntu",sans-serif;font-weight:700;font-size:15px;color:var(--black);text-align:center;line-height:22px}
.features-tab{left:130px;top:471px;width:30px;height:189px;background:var(--black)}
.features-tab span{position:absolute;left:3px;top:146px;transform:rotate(-90deg);transform-origin:left top;font-family:"Ubuntu",sans-serif;font-weight:700;font-size:18px;color:var(--yellow);width:130px}
.card{top:471px;width:239px;height:189px;background:linear-gradient(180deg,var(--yellow),var(--orange));border:1px solid var(--black);overflow:hidden}
.pic{position:absolute}
.more{position:absolute;bottom:13px;right:14px;background:var(--black);color:var(--yellow);font-size:8px;font-weight:700;padding:1px 3px;border:1px solid var(--yellow)}
.ubu{font-family:"Ubuntu",sans-serif;font-weight:700}
.divider{left:130px;top:688px;width:777px;height:1px;background:var(--black)}
.heading{font-family:"Ubuntu",sans-serif;font-weight:700;font-size:18px;color:var(--yellow);background:var(--black);padding:2px 10px;line-height:21px}
.body-copy{font-size:11.6px;line-height:13.8px;color:var(--text)}
.body-copy p{margin-bottom:13px}
.body-copy a{color:var(--link);font-weight:700;text-decoration:none}
.side-title{font-family:"Ubuntu",sans-serif;font-weight:700;font-size:18px;color:var(--black);display:flex;align-items:center;gap:10px}
.footer{left:117px;top:1081px;width:804px;height:47px;background:#2a2926;display:flex;justify-content:center;align-items:center;gap:19px;font-size:10px;color:#ddd;font-family:"Ubuntu",sans-serif}
.copyright{left:0;width:1037px;top:1147px;text-align:center;font-size:8.6px;color:var(--black)}
</style>
</head>
<body>
<div class="backdrop" role="img" aria-label="Tropical rainforest canopy background"></div>

<div class="abs page"></div>
<div class="abs header-band"></div>

<div class="abs brand"><span class="brand-dot"></span><span class="brand-name">VANTOR</span></div>
<div class="abs tagline">No Judgements. No Limits!</div>
<div class="abs account">Login<span>|</span>Register</div>
<div class="abs phone">
  <div class="phone-icon"><svg width="14" height="16" viewBox="0 0 14 16"><rect x="1" y="1" width="12" height="14" rx="2" fill="none" stroke="#111" stroke-width="2"/><rect x="4" y="4" width="6" height="3" fill="#111"/><rect x="4" y="9" width="2" height="2" fill="#111"/><rect x="8" y="9" width="2" height="2" fill="#111"/></svg></div>
  <span class="phone-num">1300 555 019</span>
</div>

<div class="abs tools"><span class="clock"></span><span>Timetable</span><span style="margin:0 6px">|</span><span>Club Locations:</span><span class="select"><span>Melbourne</span><span>▼</span></span></div>

<nav class="abs nav">
  <a class="active">HOME</a><a>ABOUT US</a><a>FITNESS</a><a>EVENTS &amp; ADVENTURES</a><a style="border:none">CONTACT US</a>
</nav>
<div class="abs social"><span></span><span></span><span></span><span></span></div>

<div class="abs hero"></div>
<div class="abs hero-photo" role="img" aria-label="Group of friends cheering with raised fists against a blue backdrop"></div>
<div class="abs hero-caption">
  <h2>Lorem Ipsum is simply dummy</h2>
  <p>Lorem Ipsum is simply dummy text of the printing and typesetting industry. Lorem Ipsum has industry's standard dummy text ever since the 1500s.</p>
</div>
<div class="abs offer">
  <h3><span class="g">Get Your</span><span class="f">FREE Membership</span><span class="t">TODAY</span></h3>
  <div class="snaps" role="img" aria-label="Snapshots of outdoor activities pinned to a line"><div></div><div></div><div></div><div></div></div>
  <div class="perks"><b>•</b> Monthly E-News Hints <b>•</b> Tips &amp; Advice<br><b>•</b> VIP Invites Events &amp; Adventures<br><b>•</b> Special Member Only Offers Discounts Card to<br>20+ Providers</div>
  <div class="field" style="left:18px;top:208px;width:252px">Your Name</div>
  <div class="field" style="left:18px;top:235px;width:152px">Your Email Address</div>
  <div class="join">» JOIN US</div>
</div>

<div class="abs features-tab"><span>FEATURES</span></div>

<div class="abs card" style="left:163px">
  <div class="pic" role="img" aria-label="Woman doing push-ups on grass" style="left:9px;top:9px;width:220px;height:170px;background:linear-gradient(135deg,#d9c9a6,#8fbf3f 60%,#4e8f1f)"></div>
  <svg class="pic" style="left:0;top:0" width="160" height="70"><polygon points="0,0 160,0 0,70" fill="#111"/></svg>
  <div class="pic ubu" style="left:10px;top:20px;transform:rotate(-24deg);color:#fff;font-size:19px">$ 80.00</div>
  <div class="pic" style="left:9px;top:131px;width:210px;height:50px;background:var(--black);padding:3px 8px">
    <div class="ubu" style="color:var(--yellow);font-size:15px">PERSONAL TRAINING</div>
    <div style="color:#fff;font-size:9px;font-weight:700">FREE Initial Consult and</div>
    <div class="ubu" style="color:#fff;font-size:13px">1-on-1 Session</div>
  </div>
  <span class="more">+MORE</span>
</div>

<div class="abs card" style="left:416px">
  <div class="pic" role="img" aria-label="Woman stretching with arms raised" style="left:110px;top:10px;width:129px;height:179px;background:linear-gradient(180deg,#e7b07a,#f5f5f5 55%,#2b2b2b)"></div>
  <div class="pic ubu" style="left:14px;top:15px;line-height:.95"><span style="font-size:16px">GROUP</span><br><span style="font-size:24px">FITNESS</span></div>
  <div class="pic ubu" style="left:15px;top:73px;font-size:12px">Intro Pass</div>
  <div class="pic ubu" style="left:17px;top:88px;background:var(--black);color:#fff;font-size:19px;padding:0 5px">$25</div>
  <div class="pic ubu" style="left:15px;top:117px;font-size:11px;line-height:1.2">7 Days<br><span style="font-size:9.5px">Unlimited Classes</span></div>
  <span class="more">+MORE</span>
</div>

<div class="abs card" style="left:668px">
  <div class="pic" role="img" aria-label="Young man running outdoors" style="left:14px;top:4px;width:125px;height:185px;background:linear-gradient(180deg,#6b4a35,#d8b49a 30%,#9aa3ad 55%,#3d4a63)"></div>
  <div class="pic ubu" style="left:114px;top:8px;background:var(--black);color:#fff;font-size:16px;padding:1px 8px">BOOT CAMP</div>
  <div class="pic ubu" style="left:129px;top:62px;color:#fff;line-height:1"><span style="font-size:15px">Start</span><br><span style="font-size:24px">SOON</span></div>
  <div class="pic ubu" style="left:129px;top:110px;color:#fff;font-size:14px;line-height:1.3">Bookings<br>are LIMITED</div>
  <span class="more">+MORE</span>
</div>

<div class="abs divider"></div>

<div class="abs heading" style="left:132px;top:711px">Personal Trainers in Brisbane</div>
<div class="abs body-copy" style="left:141px;top:744px;width:525px">
  <p>If you are exercising and have committed a good chunk of time into your fitness, you want to make sure you get the best returns possible. This is where a personal trainer can help. In personal training ses-sions you will be pushed to achieve your personal best, meaning that you get the best results, both physically and mentally, from your fitness training.</p>
  <p>For those that are new to exercising, it can be difficult to know where to begin. Having a <a>personal trainer</a> on board will give you the guidance and support that you need. Those that enlist the help of a personal trainer often find that they achieve much better results than those that go it alone, and often in a much shorter space of time.</p>
</div>

<div class="abs heading" style="left:132px;top:884px">Personal Training Locations Around Brisbane</div>
<div class="abs body-copy" style="left:144px;top:918px;width:524px">
  <p>If you are lucky enough to enjoy Brisbane's perfect climate then you shouldn't miss the chance to do some outdoor exercise. In the CBD you can enjoy a workout before work session at the Roma Street Parkland or the Brisbane City Botanic Gardens. About fifteen minutes out of town is the Mt Coot-tha Botanic Gar-dens which boast themed gardens and excellent tracks for walking and running. With plenty of beautiful parks around Brisbane's CBD, you don't need to worry about missing out on training just because of your long work hours.</p>
  <p>Just because you live in the suburbs, doesn't mean that you need to miss out on personal training either. Right around Brisbane and surrounds there are hundreds of personal trainers organizing classes in parks and in gyms and fitness studios.</p>
</div>

<div class="abs side-title" style="left:686px;top:710px">
  <svg width="26" height="24" viewBox="0 0 26 24"><rect x="1" y="8" width="24" height="15" fill="#111"/><polygon points="1,3 24,0 25,6 2,9" fill="#111"/><rect x="8" y="13" width="10" height="5" fill="#fff"/></svg>Watch Video</div>
<div class="abs" style="left:688px;top:747px;width:219px;height:148px;background:var(--black)"></div>
<div class="abs" role="img" aria-label="Runner stretching on a road, video still" style="left:695px;top:754px;width:206px;height:135px;background:linear-gradient(135deg,#cfd3d0,#8b8e8c 50%,#3d3a36)"></div>
<svg class="abs" style="left:785px;top:809px" width="26" height="26"><circle cx="13" cy="13" r="12" fill="rgba(255,255,255,.6)"/><polygon points="10,7 19,13 10,19" fill="#333"/></svg>

<div class="abs side-title" style="left:688px;top:914px">
  <svg width="32" height="26" viewBox="0 0 32 26"><polygon points="2,6 28,1 30,20 4,25" fill="#fff" stroke="#1a5a8c" stroke-width="2"/><polyline points="2,6 17,15 28,1" fill="none" stroke="#1a5a8c" stroke-width="2"/></svg>Newsletter</div>
<div class="abs" style="left:688px;top:951px;width:219px;height:87px;background:linear-gradient(180deg,var(--yellow),var(--orange-deep));border:1px solid var(--black)">
  <div class="field" style="left:14px;top:21px;width:190px">Your Email Address</div>
  <div class="abs ubu" style="left:14px;top:50px;width:106px;height:24px;background:linear-gradient(var(--yellow),var(--orange));border:1px solid var(--black);border-radius:12px;font-size:14px;font-weight:500;padding:3px 13px">Subscribe</div>
</div>

<footer class="abs footer"><span>• Home</span><span>• About Us</span><span>• Fitness</span><span>• Events &amp; Adventures</span><span>• Contact Us</span></footer>
<div class="abs copyright">Copyrights ©2011. Vantor. All Rights Reserved.</div>
</body>
</html>
```